Business Card Design Project

we want the exact same layout as your bird on fire card design with some alterations such as our logo and our contact details
Updates

This is not an open design I don't know why its showing up as such, the is a closed design meant only for QORstudio 

Industry/Entity Type

Business

Requirements
Must have
• Mr.Bartholomew Finch
CEO & Founder
ZANTHIVO
phone number 1-(555)-614-9027
Email bartholomewf@zanthivo-example.com

must be the exact same as the bird on fire design but with our logo and information.

```html
<!DOCTYPE html>
<html lang="en">
<head>
<meta charset="utf-8">
<title>ZANTHIVO — Business Card</title>
<link rel="stylesheet" href="https://fonts.googleapis.com/css2?family=Lato:wght@400;700;900&display=swap">
<style>
  :root {
    --backdrop: #3b3b3b;
    --card: #050505;
    --card-edge: #4a0d0d;
    --ink: #f2f2f2;
    --ink-soft: #c9c9c9;
    --accent: #a3261f;
    --mark-grey: #bdbdbd;
  }
  * { box-sizing: border-box; margin: 0; padding: 0; }
  html, body {
    width: 1200px; height: 900px; overflow: hidden;
    background: var(--backdrop);
    font-family: "Lato", sans-serif;
  }
  .sheet {
    position: relative; width: 1200px; height: 900px;
    display: flex; flex-direction: column; align-items: center; justify-content: center; gap: 56px;
  }
  .card {
    position: relative; width: 560px; height: 320px;
    background: var(--card);
    border-bottom: 4px solid var(--card-edge);
    box-shadow: 0 14px 30px rgba(0,0,0,.45);
    overflow: hidden;
  }
  /* Contact side */
  .identity { position: absolute; left: 44px; top: 44px; color: var(--ink); }
  .identity__name { font-size: 19px; font-weight: 400; letter-spacing: .5px; text-transform: uppercase; white-space: nowrap; }
  .identity__role, .identity__company { font-size: 13px; color: var(--ink-soft); line-height: 1.35; }
  .identity__role { margin-top: 4px; }
  .contact { position: absolute; left: 44px; top: 178px; list-style: none; color: var(--ink); font-size: 15px; }
  .contact__item { display: flex; align-items: center; gap: 12px; margin-bottom: 14px; white-space: nowrap; }
  .contact__icon { width: 14px; height: 14px; fill: var(--accent); flex: none; }
  .wordmark-small {
    position: absolute; right: 44px; top: 112px;
    color: var(--accent); font-weight: 900; font-size: 30px; letter-spacing: 3px; white-space: nowrap;
  }
  /* Brand side */
  .wordmark-large {
    position: absolute; inset: 0;
    display: flex; align-items: center; justify-content: center;
    color: var(--mark-grey); font-weight: 900; font-size: 60px; letter-spacing: 7px; white-space: nowrap;
  }
</style>
</head>
<body>
<main class="sheet">
  <section class="card card--back" aria-label="Business card, contact side">
    <div class="identity">
      <h1 class="identity__name">Mr.Bartholomew Finch</h1>
      <p class="identity__role">CEO &amp; Founder</p>
      <p class="identity__company">ZANTHIVO</p>
    </div>
    <ul class="contact">
      <li class="contact__item">
        <svg class="contact__icon" viewBox="0 0 24 24" aria-hidden="true"><path d="M6.6 10.8a15.1 15.1 0 0 0 6.6 6.6l2.2-2.2c.3-.3.7-.4 1-.2 1.1.4 2.3.6 3.6.6.6 0 1 .4 1 1V20c0 .6-.4 1-1 1A17 17 0 0 1 3 4c0-.6.4-1 1-1h3.5c.6 0 1 .4 1 1 0 1.3.2 2.5.6 3.6.1.3 0 .7-.2 1z"/></svg>
        <span>1-(555)-614-9027</span>
      </li>
      <li class="contact__item">
        <svg class="contact__icon" viewBox="0 0 24 24" aria-hidden="true"><path d="M2 5h20v14H2z M4 7v.5l8 5 8-5V7l-8 5z" fill-rule="evenodd"/></svg>
        <span>bartholomewf@zanthivo-example.com</span>
      </li>
    </ul>
    <div class="wordmark-small">ZANTHIVO</div>
  </section>

  <section class="card card--front" aria-label="Business card, brand side">
    <div class="wordmark-large">ZANTHIVO</div>
  </section>
</main>
</body>
</html>
```